Business card design needed

Velisse Pure, Safe, Beneficial

Tree on one side as the skin care is based on botanical.

Velisse is a highly regarded premium brand with a Swiss heritage. The product are healthy botanically based and inspired by nature.

Target Market(s)

females

Industry/Entity Type

Business

Contact Information for Business Card

Velisse

Harriet Coyle
Velisse Independent Consultant
0427 358 104

hcoyle7@brimnet.example.au

Requirements
Must have
• Velisse
Nice to have
• nice shape tree or plants, flowers

```html
<!DOCTYPE html>
<html lang="en">
<head>
<meta charset="utf-8">
<title>Velisse – Harriet Coyle business card</title>
<link href="https://fonts.googleapis.com/css2?family=Delius&family=Mulish:wght@400;700;800&display=swap" rel="stylesheet">
<style>
  :root {
    --page-bg: #ececea;
    --card-bg: #ffffff;
    --ink: #111111;
    --ink-soft: #6b6b6b;
    --lavender: #b3a6d8;
    --petal-orange: #f0481a;
    --petal-deep: #d8340f;
    --petal-yellow: #e9ef1e;
    --petal-white: #e9ecef;
    --centre-gold: #f2c640;
    --brand-ink: #7a4fa0;
  }
  * { box-sizing: border-box; margin: 0; padding: 0; }
  html, body {
    width: 1200px; height: 1200px; overflow: hidden;
    background: var(--page-bg);
  }
  .card {
    position: absolute;
    left: 100px; top: 324px;
    width: 1000px; height: 552px;
    background: var(--card-bg);
    overflow: hidden;
    box-shadow: 0 6px 24px rgba(0,0,0,0.12);
  }
  .card__flower {
    position: absolute;
    left: 0; top: 0;
    width: 500px; height: 552px;
    background:
      radial-gradient(circle at 8% 92%, var(--centre-gold) 0 60px, transparent 61px),
      radial-gradient(ellipse 330px 360px at 8% 92%, var(--petal-orange) 0 70%, var(--petal-deep) 85%, transparent 86%),
      radial-gradient(ellipse 220px 200px at 18% 10%, var(--petal-yellow) 0 70%, transparent 72%),
      radial-gradient(ellipse 280px 300px at 60% 30%, var(--petal-white) 0 65%, transparent 70%),
      var(--card-bg);
  }
  .card__brand {
    position: absolute;
    right: 80px; top: 90px;
    width: 260px;
    text-align: center;
    font-family: "Mulish", sans-serif;
    font-weight: 700;
    font-size: 52px;
    letter-spacing: 2px;
    color: var(--brand-ink);
  }
  .card__details {
    position: absolute;
    right: 56px; top: 272px;
    text-align: right;
    font-family: "Mulish", sans-serif;
  }
  .card__name {
    font-family: "Delius", cursive;
    font-size: 36px;
    color: var(--ink-soft);
    letter-spacing: 1px;
    line-height: 1.2;
  }
  .card__company {
    font-weight: 700;
    font-size: 31px;
    color: var(--ink);
    line-height: 1.2;
  }
  .card__role {
    font-size: 26px;
    color: var(--lavender);
    line-height: 1.25;
    margin-bottom: 16px;
  }
  .card__phone {
    font-weight: 800;
    font-size: 36px;
    color: var(--ink);
    line-height: 1.3;
  }
  .card__email {
    font-weight: 700;
    font-size: 25px;
    color: var(--ink);
    line-height: 1.4;
  }
</style>
</head>
<body>
  <main class="card">
    <div class="card__flower" role="img" aria-label="Close-up photograph of orange, yellow and white gerbera daisy petals"></div>
    <div class="card__brand">Velisse</div>
    <div class="card__details">
      <p class="card__name">Harriet Coyle</p>
      <p class="card__company">Velisse</p>
      <p class="card__role">Independent Consultant</p>
      <p class="card__phone">0427 358 104</p>
      <p class="card__email">hcoyle7@brimnet.example.au</p>
    </div>
  </main>
</body>
</html>
```